Values Statement poster template

We want to develop a poster template for our company policies and statements which promote our company values in our workplaces.
These documents are important in showing our clients, suppliers and employees who we are and what we stand for.
The graphic design will incorporate our company logo, and be bright, uplifting and inspiring, developing a graphic theme that we can utilise for other company documents. The design will graphically illustrate and support our values statement, with colour and modern design.
This values poster will be the first in a series of documents using the same theme.The format will be a4 and a3 portrait
We are an environmental service business specialising in rehabilitation and revegetation

Target Market(s)

Tier one clients in industry, Mining, Construction and agriculture

Font styles to use
Other font styles liked:
• calibri

Requirements
Must have
• Professional , high end feel, able to read clearly on a poster
Nice to have
• graphic design elements, symbols, etc which support the message, that can be carried through to various documents such as quality, environmental, safety policies
A bright theme which ties in with our logo colours.

```html
<!DOCTYPE html>
<html lang="en">
<head>
<meta charset="utf-8">
<title>Values Statement Poster</title>
<link href="https://fonts.googleapis.com/css2?family=Arimo:wght@400;700&family=Montserrat+Alternates:ital,wght@0,700;1,400;1,700&family=Nunito:wght@700&display=swap" rel="stylesheet">
<style>
  :root {
    --bg: #ecebe8;
    --paper: #ffffff;
    --ink: #1a1a1a;
    --brand-green: #0b5a2a;
    --brand-orange: #e0661b;
    --accent-teal: #1a9bb5;
    --photo-dark: #1c2d55;
    --photo-light: #9fb8d3;
    --rule: #333333;
  }
  * { box-sizing: border-box; margin: 0; padding: 0; }
  html, body { width: 1200px; height: 1200px; overflow: hidden; background: var(--bg); }
  body { position: relative; font-family: "Arimo", Arial, sans-serif; color: var(--ink); }

  .poster {
    position: absolute; left: 190px; top: 20px;
    width: 820px; height: 1160px;
    background: var(--paper);
    box-shadow: 0 6px 24px rgba(0,0,0,.15);
    overflow: hidden;
  }

  .hero-photo {
    position: absolute; left: 0; top: 0; width: 820px; height: 440px;
    background: linear-gradient(110deg, var(--photo-light) 0%, #6f8fb3 38%, #34507f 62%, var(--photo-dark) 100%);
  }
  .brand-name {
    position: absolute; left: 52px; top: 140px;
    font-family: "Nunito", sans-serif; font-weight: 700;
    font-size: 44px; color: var(--brand-green);
    display: flex; align-items: center; gap: 12px;
  }
  .brand-name .brand-dot {
    width: 30px; height: 30px; border-radius: 50%; background: var(--brand-orange);
  }

  .column { position: absolute; top: 462px; }
  .column.left { left: 36px; width: 370px; }
  .column.right { left: 440px; width: 350px; }

  .intro { border-left: 12px solid var(--accent-teal); padding-left: 12px; margin-bottom: 34px; }
  .intro-title {
    font-family: "Montserrat Alternates", sans-serif; font-weight: 700; font-style: italic;
    font-size: 28px; display: flex; align-items: flex-end; gap: 6px;
  }
  .intro-title::after { content: ""; flex: 1; border-bottom: 1.5px solid var(--rule); margin-bottom: 6px; }
  .intro-sub, .lead {
    font-family: "Montserrat Alternates", sans-serif; font-style: italic; font-weight: 400;
    font-size: 20px; line-height: 22px;
  }

  .section { margin-bottom: 24px; }
  .section h2 {
    font-family: "Montserrat Alternates", sans-serif; font-style: italic; font-weight: 700;
    font-size: 21px; line-height: 26px;
  }
  .section h2 .light { font-weight: 400; }
  .section h2.ruled { display: flex; align-items: flex-end; gap: 6px; }
  .section h2.ruled::after { content: ""; flex: 1; border-bottom: 1.5px solid var(--rule); margin-bottom: 6px; }
  .section .kicker { font-size: 10.5px; font-weight: 700; margin: 8px 0 4px; }
  .section p { font-size: 10.5px; line-height: 14px; margin-top: 8px; }
  .section .lead { margin-top: 10px; font-size: 22px; line-height: 24px; }

  .values-list { list-style: none; font-size: 10.5px; line-height: 14px; }
  .values-list li { position: relative; padding-left: 12px; }
  .values-list li::before {
    content: ""; position: absolute; left: 0; top: 4px;
    width: 5px; height: 5px; border: 1.5px solid var(--brand-orange); border-radius: 50%;
  }

  .footer-band { position: absolute; left: 0; bottom: 0; width: 820px; height: 160px; }
  .footer-mark {
    position: absolute; right: 40px; bottom: 40px;
    width: 34px; height: 34px; border-radius: 50%; border: 3px solid var(--paper);
  }
</style>
</head>
<body>
  <main class="poster">
    <div class="hero-photo" role="img" aria-label="Photo of two businessmen in suits reviewing a tablet in a bright office"></div>
    <div class="brand-name"><span class="brand-dot"></span>Verdantia</div>

    <section class="column left">
      <div class="intro">
        <h1 class="intro-title">Values</h1>
        <p class="intro-sub">These are the things<br>we value most,<br>they define the way<br>we do business</p>
      </div>

      <div class="section">
        <h2>We Value our People<br><span class="light">Above Everything Else</span></h2>
        <p class="kicker">We demonstrate this by:</p>
        <ul class="values-list">
          <li>Providing safe, positive, enjoyable workplaces where everyone feels valued and respected</li>
          <li>Providing Careers, not Jobs, we grow together</li>
          <li>Encouraging inclusion, participation and collaboration</li>
          <li>Recognising and rewarding contribution and excellence</li>
          <li>Supporting our people through tough times</li>
        </ul>
      </div>

      <div class="section">
        <h2>We do Good Things</h2>
        <h2 class="ruled"><span class="light">for The Planet</span></h2>
        <p class="lead">Our products are helping revegetate Australia, which we are tremendously proud of. We minimise our environmental impact in everything we do.</p>
      </div>

      <div class="section">
        <h2>We set the Standard</h2>
        <ul class="values-list">
          <li>We are uncompromising on quality</li>
          <li>We are the best at what we do, and we do what we are best at</li>
          <li>We are always improving</li>
          <li>We are pioneering</li>
        </ul>
      </div>
    </section>

    <section class="column right">
      <div class="section">
        <h2>Our Workplaces are Safe</h2>
        <p>There is nothing more important to us than our people going home healthy and safe every day. We won't accept anything less. We believe safety is a management choice. By providing safe work systems, and education we achieve our daily goal of Zero Harm. At Verdantia we;</p>
        <ul class="values-list" style="margin-top:6px">
          <li>Take the time to make our work areas safe, whatever it takes</li>
          <li>Don't accept shortcuts</li>
          <li>Look out for each other</li>
          <li>Investigate our incidents and learn from them, we won't accept repeats</li>
          <li>Are constantly looking for ways to improve the safety of our workplaces.</li>
          <li>Think safe, work safer, go home safe!</li>
        </ul>
      </div>

      <div class="section">
        <h2><span class="light">We are Proud of</span> Who We Are</h2>
        <p class="kicker">Our reputation means the world to us. we:</p>
        <ul class="values-list">
          <li>Treat everyone with respect and we expect it in return</li>
          <li>Follow the rules</li>
          <li>Do what we say we will do</li>
          <li>Own our mistakes and we fix them</li>
          <li>Are trustworthy and transparent</li>
        </ul>
      </div>

      <div class="section">
        <h2><span class="light">We</span> Succeed Together</h2>
        <p>We believe in win-win relationships. When our business is profitable everyone benefits, our owners, employees, clients and the community. at <b>Verdantia we:</b></p>
        <ul class="values-list" style="margin-top:6px">
          <li>Work as a team, we get it done together</li>
          <li>We treat our suppliers and subcontractors like they are part of the team.</li>
          <li>Are building on our success, and growing together</li>
          <li>Choose to work with employees, customers and suppliers who fit our values</li>
        </ul>
      </div>

      <div class="section">
        <h2>We Give Back</h2>
        <p>We appreciate our success and we give back by supporting our community, and those less fortunate.</p>
      </div>
    </section>

    <svg class="footer-band" viewBox="0 0 820 160" preserveAspectRatio="none" aria-hidden="true">
      <path d="M0 150 C 300 140, 560 110, 820 20 L 820 160 L 0 160 Z" fill="var(--brand-green)"/>
      <path d="M0 120 C 200 118, 400 108, 560 82 C 420 110, 220 126, 0 134 Z" fill="var(--brand-orange)"/>
    </svg>
    <div class="footer-mark"></div>
  </main>
</body>
</html>
```